Dutch psychology podcast needs logo / art design

I need a logo / artwork for my new podcast on psychology/health called 'Het Stille Kompas'. In the podcast I talk to different experts on subjects as personal development, psychology, health, spirituality and entrepreneurship. I would like to see my brand colors back in the design (www.joristeulinghof.nl) and my face in the artwork since I'm the host of the show.

My photo is included in the attachments and I've also added some examples of what I'm looking for.

Industry/Entity Type

Psychology

Colors

Designer to choose colors to be used in the design.

Requirements
Must have
• - Name of the show: 'Het Stille Kompas' (I prefer that this name is turned into a logo), see attachment of example of Harbor of Quiet Minds
• - Subtitle: 'met Joris Teulinghof' which is my name a the host
• - My picture, see attachments

```html
<!DOCTYPE html>
<html lang="nl">
<head>
<meta charset="utf-8">
<title>Het Stille Kompas – podcast artwork</title>
<link href="https://fonts.googleapis.com/css2?family=Anton&family=Cinzel:wght@600&display=swap" rel="stylesheet">
<style>
  :root {
    --backdrop: #e4e4e4;
    --green-light: #4fa00f;
    --green-mid: #3a8a0a;
    --green-dark: #245a05;
    --green-shadow: #173a05;
    --gold-glow: #f7dc2c;
    --gold-mid: #d9a021;
    --gold-deep: #7a4b12;
    --blue-glow: #1b6f95;
    --blue-mid: #0c2f52;
    --blue-deep: #050b1a;
    --skin: #c98a68;
    --skin-shade: #8a5238;
    --hair: #1c1512;
    --shirt: #06070f;
    --white: #ffffff;
  }
  html, body {
    margin: 0;
    padding: 0;
    width: 1200px;
    height: 1200px;
    overflow: hidden;
    background: var(--backdrop);
  }
  .cover {
    position: absolute;
    left: 344px;
    width: 512px;
    height: 512px;
    overflow: hidden;
  }
  .cover--warm { top: 63px; }
  .cover--night { top: 620px; }

  .cover__backdrop {
    position: absolute;
    inset: 0 0 96px 0;
  }
  .cover--warm .cover__backdrop {
    background:
      radial-gradient(circle at 48% 48%, var(--gold-glow) 0%, var(--gold-mid) 38%, transparent 70%),
      linear-gradient(160deg, var(--gold-mid) 0%, var(--gold-deep) 100%);
  }
  .cover--night .cover__backdrop {
    background:
      radial-gradient(circle at 40% 30%, var(--blue-glow) 0%, var(--blue-mid) 40%, transparent 72%),
      linear-gradient(160deg, var(--blue-mid) 0%, var(--blue-deep) 100%);
  }

  /* host portrait area: head, neck and dark shirt in flat tones */
  .host-portrait {
    position: absolute;
    left: 0;
    top: 24px;
    width: 360px;
    height: 392px;
  }
  .host-portrait__head {
    position: absolute;
    left: 96px;
    top: 0;
    width: 148px;
    height: 220px;
    border-radius: 46% 46% 44% 44%;
    background: linear-gradient(180deg, var(--hair) 0%, var(--hair) 18%, var(--skin) 26%, var(--skin) 70%, var(--skin-shade) 100%);
  }
  .host-portrait__shirt {
    position: absolute;
    left: 0;
    top: 238px;
    width: 360px;
    height: 154px;
    border-radius: 120px 150px 0 0;
    background: var(--shirt);
  }

  .title-ribbon {
    position: absolute;
    display: flex;
    align-items: center;
    padding-left: 28px;
    box-sizing: border-box;
    background: linear-gradient(90deg, var(--green-light), var(--green-mid) 60%, var(--green-dark));
    color: var(--white);
    font-family: 'Anton', sans-serif;
    line-height: 1;
    transform: rotate(-5deg);
    box-shadow: 3px 4px 0 var(--green-shadow);
    text-shadow: 1px 2px 2px rgba(0,0,0,0.35);
  }
  .title-ribbon--first  { left: 232px; top: 58px;  width: 156px; height: 64px; font-size: 50px; }
  .title-ribbon--second { left: 258px; top: 112px; width: 236px; height: 76px; font-size: 60px; }
  .title-ribbon--third  { left: 244px; top: 190px; width: 190px; height: 72px; font-size: 58px; padding-left: 40px; }

  .host-band {
    position: absolute;
    left: 0; right: 0; bottom: 0;
    height: 96px;
    display: flex;
    align-items: center;
    justify-content: center;
    background: linear-gradient(90deg, var(--green-dark), var(--green-mid) 50%, var(--green-dark));
    color: var(--white);
    font-family: 'Cinzel', serif;
    font-weight: 600;
    font-size: 27px;
    letter-spacing: 0.5px;
  }
</style>
</head>
<body>

<section class="cover cover--warm">
  <div class="cover__backdrop" role="img" aria-label="Warm golden glow with a sketched city skyline"></div>
  <div class="host-portrait" role="img" aria-label="Host portrait photo, smiling man in a dark T-shirt">
    <div class="host-portrait__shirt"></div>
    <div class="host-portrait__head"></div>
  </div>
  <div class="title-ribbon title-ribbon--first">Het</div>
  <div class="title-ribbon title-ribbon--second">Stille</div>
  <div class="title-ribbon title-ribbon--third">Kompas</div>
  <div class="host-band">MET JORIS TEULINGHOF</div>
</section>

<section class="cover cover--night">
  <div class="cover__backdrop" role="img" aria-label="Deep blue glow with a dark city skyline"></div>
  <div class="host-portrait" role="img" aria-label="Host portrait photo, smiling man in a dark T-shirt">
    <div class="host-portrait__shirt"></div>
    <div class="host-portrait__head"></div>
  </div>
  <div class="title-ribbon title-ribbon--first">Het</div>
  <div class="title-ribbon title-ribbon--second">Stille</div>
  <div class="title-ribbon title-ribbon--third">Kompas</div>
  <div class="host-band">MET JORIS TEULINGHOF</div>
</section>

</body>
</html>
```